Poster for List of Company Values

We need a poster to outline our Values which will be displayed in our office as well as posted on our website and other platforms (so need to allow for some flexibly in its application).

File attached outlines what we currently have with design and also our company style guide.

Note that we are looking for a modern, clean look, which still represents our core activities of construction and environmental services.

You can also reference our website here:

https://quorvelgroup.com.au/

Happy to answer any questions you might have.

Thanks for your interest,
Brent

Target Market(s)

Internal and External clients

Industry/Entity Type

Construction, water and recycling

Font styles to use
Sans Serif

Requirements
Must have
• All values on the one page. Graphic to represent each value. Also needs to use company logo
Nice to have
• Preference for poster to be orientated in landscape
Should not have
• Do not follow example provided, this is only to demonstrate what we have to date and also the text required

```html
<!DOCTYPE html>
<html lang="en">
<head>
<meta charset="utf-8">
<title>Halvern Group — Our Values</title>
<link href="https://fonts.googleapis.com/css2?family=Montserrat:wght@300;400;700;800;900&family=Open+Sans:ital,wght@1,600&display=swap" rel="stylesheet">
<style>
  :root {
    --backdrop: #161616;
    --teal: #3fae97;
    --green: #56a73e;
    --navy: #233f85;
    --crimson: #c82b4a;
    --orange: #e8884b;
    --gold: #ddc55d;
    --olive: #5b5329;
    --white: #ffffff;
  }
  * { margin: 0; padding: 0; box-sizing: border-box; }
  html, body {
    width: 1200px;
    height: 1200px;
    overflow: hidden;
    background: var(--backdrop);
  }
  .values-board {
    position: relative;
    width: 1200px;
    height: 1200px;
  }
  .value-card {
    position: absolute;
    width: 274px;
    height: 388px;
    color: var(--white);
    overflow: hidden;
  }
  .col-1 { left: 168px; }
  .col-2 { left: 463px; }
  .col-3 { left: 758px; }
  .row-1 { top: 201px; }
  .row-2 { top: 611px; }

  .card-loyal { background: var(--teal); }
  .card-initiative { background: var(--green); }
  .card-team { background: var(--navy); }
  .card-respect { background: var(--crimson); }
  .card-open { background: var(--orange); }
  .card-positive { background: var(--gold); color: var(--olive); }

  .brand {
    position: absolute;
    top: 26px;
    left: 0;
    right: 0;
    display: flex;
    align-items: center;
    justify-content: center;
    gap: 6px;
    font-family: "Montserrat", sans-serif;
    font-weight: 700;
    font-size: 11px;
    letter-spacing: 2px;
  }
  .brand-square {
    width: 7px;
    height: 7px;
    background: currentColor;
  }
  .value-icon {
    position: absolute;
    top: 60px;
    left: 50%;
    width: 52px;
    height: 52px;
    margin-left: -26px;
    fill: none;
    stroke: currentColor;
    stroke-width: 3;
    stroke-linecap: round;
    stroke-linejoin: round;
  }
  .value-statement {
    position: absolute;
    top: 130px;
    left: 8px;
    right: 8px;
    text-align: center;
    font-family: "Open Sans", sans-serif;
    font-style: italic;
    font-weight: 600;
    font-size: 14.5px;
    line-height: 20px;
  }
  .value-title {
    position: absolute;
    left: 16px;
    bottom: 16px;
    font-family: "Montserrat", sans-serif;
    line-height: 0.78;
    text-transform: uppercase;
  }
  .value-title span { display: block; }
  .lead { font-weight: 300; }
  .key { font-weight: 900; letter-spacing: -1.5px; }

  .card-loyal .lead { font-size: 66px; }
  .card-loyal .key { font-size: 70px; margin-top: 2px; }
  .card-initiative .lead { font-size: 36px; }
  .card-initiative .key { font-size: 45px; margin-top: 4px; }
  .card-team .lead { font-size: 36px; }
  .card-team .key { font-size: 80px; margin-top: 4px; }
  .card-respect .lead { font-size: 34px; }
  .card-respect .key { font-size: 51px; margin-top: 4px; }
  .card-open .value-title { line-height: 0.8; }
  .card-open .lead { font-size: 42px; }
  .card-open .key { font-size: 54px; margin-top: 2px; }
  .card-positive .lead { font-size: 44px; }
  .card-positive .key { font-size: 49px; margin-top: 4px; }
</style>
</head>
<body>
<main class="values-board">

  <section class="value-card card-loyal col-1 row-1">
    <div class="brand"><span class="brand-square"></span>HALVERN</div>
    <svg class="value-icon" viewBox="0 0 52 52" aria-hidden="true">
      <path d="M26 6 L42 12 V25 C42 35 35 42 26 46 C17 42 10 35 10 25 V12 Z"/>
      <path d="M19 26 L24 31 L33 21"/>
    </svg>
    <p class="value-statement">We take care of our own and<br>provide opportunities to listen<br>and support each other.</p>
    <h2 class="value-title"><span class="lead">Be</span><span class="key">Loyal</span></h2>
  </section>

  <section class="value-card card-initiative col-2 row-1">
    <div class="brand"><span class="brand-square"></span>HALVERN</div>
    <svg class="value-icon" viewBox="0 0 52 52" aria-hidden="true">
      <path d="M8 40 L20 28 L28 34 L44 14"/>
      <path d="M34 14 H44 V24"/>
    </svg>
    <p class="value-statement">We celebrate and<br>recognize our own and<br>encourage forward thinking.</p>
    <h2 class="value-title"><span class="lead">Show</span><span class="key">Initiative</span></h2>
  </section>

  <section class="value-card card-team col-3 row-1">
    <div class="brand"><span class="brand-square"></span>HALVERN</div>
    <svg class="value-icon" viewBox="0 0 52 52" aria-hidden="true">
      <circle cx="26" cy="16" r="6"/>
      <circle cx="12" cy="22" r="5"/>
      <circle cx="40" cy="22" r="5"/>
      <path d="M16 42 C16 32 36 32 36 42"/>
      <path d="M4 40 C4 32 14 31 17 34"/>
      <path d="M48 40 C48 32 38 31 35 34"/>
    </svg>
    <p class="value-statement">We communicate effectively and<br>work as a team by helping and<br>supporting each other.</p>
    <h2 class="value-title"><span class="lead">Think</span><span class="key">Team</span></h2>
  </section>

  <section class="value-card card-respect col-1 row-2">
    <div class="brand"><span class="brand-square"></span>HALVERN</div>
    <svg class="value-icon" viewBox="0 0 52 52" aria-hidden="true">
      <circle cx="19" cy="26" r="12"/>
      <circle cx="33" cy="26" r="12"/>
    </svg>
    <p class="value-statement">We value the diversity and<br>opinions of all.</p>
    <h2 class="value-title"><span class="lead">Show</span><span class="key">Respect</span></h2>
  </section>

  <section class="value-card card-open col-2 row-2">
    <div class="brand"><span class="brand-square"></span>HALVERN</div>
    <svg class="value-icon" viewBox="0 0 52 52" aria-hidden="true">
      <path d="M10 44 V8 H38 V44"/>
      <path d="M10 8 L28 14 V48 L10 44"/>
      <path d="M4 44 H46"/>
    </svg>
    <p class="value-statement">We are clear and open with each<br>other, and provide an approachable<br>and friendly environment.</p>
    <h2 class="value-title"><span class="lead">Be</span><span class="key">Open</span><span class="lead">And</span><span class="key">Honest</span></h2>
  </section>

  <section class="value-card card-positive col-3 row-2">
    <div class="brand"><span class="brand-square"></span>HALVERN</div>
    <svg class="value-icon" viewBox="0 0 52 52" aria-hidden="true">
      <circle cx="26" cy="26" r="9"/>
      <path d="M26 5 V11 M26 41 V47 M5 26 H11 M41 26 H47 M11 11 L15 15 M37 37 L41 41 M41 11 L37 15 M15 37 L11 41"/>
    </svg>
    <p class="value-statement">SMILE<br>We are solutions focused and<br>encourage a positive attitude<br>turning a negative into a positive.</p>
    <h2 class="value-title"><span class="lead">Be</span><span class="key">Positive</span></h2>
  </section>

</main>
</body>
</html>
```